Harborline Coverage (02)

We're designing a website to sell Medicare Supplements. Attached is the content we want to say and general layout, but please use your best knowledge to make it better. This platform is intentionally simplistic because this is reaching an older demographic, so it should be very straightforward, attention-grabbing and extremely user-friendly, while still appearing reliable and professional.
This should be a two-page web design. The homepage has information on Medicare supplements (script in image attached below) along with a button to input zip code. This triggers a window to pop up asking for personal information (will also be listed in attachment).
This brings you to the second page that lists out the medicare supplement companies and plans based on inputed information. We just want to see the design you have in mind, so it doesn't matter what information you put in this section. Feel free to reference/replicate the information in image 3 in the doc. There should be a section where you can filter results by company, premium price, or coverage plans.
Target Market(s)
Seniors, 65+
Industry/Entity Type
Insurance
Number of Pages Required
2 page
Look and feel
Each slider illustrates characteristics of the customer's brand and the style your logo design should communicate.

```html
<!DOCTYPE html>
<html lang="en">
<head>
<meta charset="utf-8">
<title>Harborline Coverage — Get a Quote</title>
<link href="https://fonts.googleapis.com/css2?family=Raleway:wght@400;500;600;700;800&display=swap" rel="stylesheet">
<style>
  :root{
    --teal:#1e6a85;
    --teal-bar:#6aabc4;
    --green:#0aa84f;
    --logo-green:#2fae5a;
    --page:#f0f0f0;
    --field:#e4e4e4;
    --muted:#6b6b6b;
    --placeholder:#8a8a8a;
    --white:#ffffff;
    --dark-green:#0f4d2a;
  }
  *{box-sizing:border-box;margin:0;padding:0}
  html,body{width:1200px;height:1160px;overflow:hidden;background:var(--page);font-family:"Raleway",sans-serif}
  .canvas{position:relative;width:1200px;height:1160px;overflow:hidden;background:var(--page)}
  .info-bar{position:absolute;top:0;left:0;width:1200px;height:25px;background:var(--teal-bar);color:var(--white);font-size:13.5px;text-align:center;line-height:25px}
  .info-bar strong{font-weight:700}
  .site-header{position:absolute;top:25px;left:0;width:1200px;height:83px;background:var(--page)}
  .brand{position:absolute;left:170px;top:30px;font-size:21px;font-weight:700;color:var(--teal);letter-spacing:.5px}
  .hero{position:absolute;top:108px;left:0;width:1200px;height:679px;
    background:radial-gradient(ellipse at 70% 10%,#b6cfd6 0%,#7fb3c6 25%,transparent 45%),
               radial-gradient(ellipse at 5% 40%,#9ec0cc 0%,#5e8fa3 30%,transparent 55%),
               linear-gradient(100deg,#1d4e63 0%,#3d7f98 30%,#6aabc4 60%,#6aabc4 100%)}
  .menu-toggle{position:absolute;left:1044px;top:104px}
  .benefits{position:absolute;left:225px;width:750px;color:var(--teal);font-size:21px;text-align:center;line-height:26px}
  .benefits b{font-weight:700}
  .benefit-item{position:absolute;left:360px;top:1138px;font-size:18px;color:var(--dark-green)}
  .benefit-item b{font-weight:700}
  .benefit-dot{position:absolute;left:359px;top:1138px}
  .quote-modal{position:absolute;left:260px;top:245px;width:678px;height:817px;background:var(--white);border-radius:14px;box-shadow:0 6px 24px rgba(0,0,0,.12)}
  .quote-title{position:absolute;left:34px;top:32px;font-size:21px;font-weight:700;color:var(--teal)}
  .quote-lead{position:absolute;left:34px;top:78px;width:620px;font-size:17.5px;line-height:22px;color:var(--muted);text-transform:uppercase}
  .quote-note{position:absolute;left:36px;top:128px;width:610px;font-size:13px;line-height:17.5px;color:var(--muted);text-transform:uppercase}
  .section-label{position:absolute;font-size:17.5px;color:var(--teal);text-transform:uppercase;display:flex;align-items:center;gap:9px}
  .section-label svg{flex:none}
  .choice{position:absolute;left:41px;font-size:14px;color:var(--teal);display:flex;align-items:center;gap:7px}
  .choice i{display:block;width:11px;height:11px;border:1.6px solid var(--teal)}
  .field{position:absolute;height:39px;background:var(--field);border-radius:6px;color:var(--placeholder);font-size:19px;line-height:39px;padding-left:20px}
  .field-label{position:absolute;font-size:14px;color:var(--teal)}
  .field-label sup{font-size:8px}
  .compare-btn{position:absolute;left:47px;top:737px;width:185px;height:36px;background:var(--green);color:var(--white);border-radius:5px;font-size:17.5px;line-height:36px;text-align:center;text-transform:uppercase}
</style>
</head>
<body>
<div class="canvas">
  <div class="info-bar"><strong>CALL (800) 555-0142</strong> FOR MORE INFORMATION</div>
  <header class="site-header">
    <div class="brand">HARBORLINE COVERAGE</div>
  </header>
  <div class="hero" role="img" aria-label="Photo of a smiling senior customer in a bright setting"></div>
  <svg class="menu-toggle" width="20" height="12" viewBox="0 0 20 12"><path d="M2 2 L10 9 L18 2" fill="none" stroke="#1e6a85" stroke-width="2.5"/></svg>

  <p class="benefits" style="top:966px">Each Medicare Supplement plan covers a set of<br>basic benefits that Original Medicare has not covered</p>
  <p class="benefits" style="top:1047px"><b>Medicare Supplement Insurance Plans</b> do not always cover vision,<br>dental, long-term care, or hearing aids, but all plans must cover at least a<br>portion of the following basic benefits:</p>
  <svg class="benefit-dot" width="32" height="32" viewBox="0 0 32 32" style="left:359px;top:1139px"><circle cx="16" cy="16" r="13" fill="none" stroke="#0f4d2a" stroke-width="3"/><circle cx="16" cy="16" r="7" fill="#0f4d2a"/></svg>
  <div class="benefit-item" style="left:405px"><b>Medicare Part A Coinsurance</b> costs up to an</div>

  <section class="quote-modal">
    <h1 class="quote-title">GET A QUOTE</h1>
    <p class="quote-lead">To figure out what your monthly premium would be, enter your gender and date of birth</p>
    <p class="quote-note">Lorem ipsum dolor sit amet, consectetur adipiscing elit, sed do eiusmod tempor incididunt ut labore et dolore magna aliqua. Quis ipsum sus-pendisse ultrices gravida. Risus commodo viverra maecenas accumsan lacus vel facilisis.</p>

    <div class="section-label" style="left:40px;top:237px"><svg width="14" height="11" viewBox="0 0 14 11"><path d="M0 0H14L7 11Z" fill="#1e6a85"/></svg>Gender</div>
    <div class="choice" style="top:270px"><i></i>Male</div>
    <div class="choice" style="top:290px"><i></i>Female</div>

    <div class="section-label" style="left:41px;top:319px"><svg width="14" height="11" viewBox="0 0 14 11"><path d="M0 0H14L7 11Z" fill="#1e6a85"/></svg>Date of Birth</div>
    <div class="field" style="left:42px;top:350px;width:184px">mm/dd/yyyy</div>

    <div class="section-label" style="left:44px;top:403px"><svg width="14" height="11" viewBox="0 0 14 11"><path d="M0 0H14L7 11Z" fill="#1e6a85"/></svg>Hospital Insurance (Part A)</div>
    <div class="field-label" style="left:48px;top:441px">Part A Month<sup>*</sup></div>
    <div class="field-label" style="left:249px;top:441px">Part A Year<sup>*</sup></div>
    <div class="field" style="left:47px;top:471px;width:185px">month</div>
    <div class="field" style="left:243px;top:471px;width:184px">year</div>

    <div class="section-label" style="left:44px;top:524px"><svg width="14" height="11" viewBox="0 0 14 11"><path d="M0 0H14L7 11Z" fill="#1e6a85"/></svg>Medical Insurance (Part B)</div>
    <div class="field-label" style="left:51px;top:561px">Part B Month<sup>*</sup></div>
    <div class="field-label" style="left:252px;top:561px">Part B Year<sup>*</sup></div>
    <div class="field" style="left:47px;top:592px;width:185px">month</div>
    <div class="field" style="left:243px;top:592px;width:184px">year</div>

    <div class="section-label" style="left:45px;top:651px"><svg width="14" height="11" viewBox="0 0 14 11"><path d="M0 0H14L7 11Z" fill="#1e6a85"/></svg>Desired Coverage Start Date</div>
    <div class="field" style="left:47px;top:680px;width:185px">mm/dd/yyyy</div>

    <div class="compare-btn">Compare Rates</div>
  </section>
</div>
</body>
</html>
```